Medical Billing and Professional Services

We are a full-service medical billing company, utilizing state-of-the art software to analyze, code, and electronically bill commercial and government subsidized insurance companies for physicians' services provided to patients. We bill both hospital and private clinics' claims directly to the appropriate carrier, with reduced turn-around times, increased cash flow, and greater profitability to the physician or practice. We customize every client's pricing to their specific practice, and the services they might require. Generally, we operate on a percentage basis of the allowed charges for particular procedure, but also can arrange monthly or per claim pricing. We can manage A/R, and work with a collection company that goes after delinquents. WE ARE NOT A COLLECTION AGENCY, and do not represent ourselves as such. However, our company practices do eliminate much of the need for such.
We follow up, follow up, and follow up until a claim is paid in full, according to contractual schedules. We also eliminate the practice's need to spend hours on the phone to resolve unpaid claims, thus reducing labor, equipment, and computer costs. In essence, more money to the bottom line for the practice.
However, we almost never gain a client without a meeting. There are many online services, but our strength is personal relationship. The owner ALWAYS meets with the doctors or office manager. Our success depends on getting the practice paid in full for their services. (Which we do 99.2% of the time).
We also offer notary service, when needed.

Target Market(s)

physicians in private practice, also chiropractors, and doctors not employed by hospitals or clinics.

Industry/Entity Type

Government

Requirements
Must have
• attractive colors, basic information about the benefits of using a billing service.. Call to action is very important. Our reach out in the past has been: "You care for your patients, WE care for your practice."
Nice to have
• focus on electronics and new technology, which we have. Also our reputation with current clients, and 12 years of experience.
Should not have
• no old fonts, money icons or references to gold or money.

```html
<!DOCTYPE html>
<html lang="en">
<head>
<meta charset="utf-8">
<title>Harbor Claims Medical Billing Flyers</title>
<link rel="stylesheet" href="https://fonts.googleapis.com/css2?family=Bebas+Neue&family=Open+Sans:ital,wght@0,400;0,600;0,700;1,700&display=swap">
<style>
  :root {
    --backdrop: #5e0707;
    --white: #ffffff;
    --ink: #1e2a26;
    --teal-photo-a: #4f8f72;
    --teal-photo-b: #a9cfa9;
    --teal-panel: #80b9a0;
    --teal-sweep: #e6efe9;
    --olive-photo-a: #9aa04a;
    --olive-photo-b: #d6df8a;
    --olive-panel: #b3c46a;
    --olive-sweep: #6f7428;
  }
  * { margin: 0; padding: 0; box-sizing: border-box; }
  html, body { width: 1200px; height: 1000px; overflow: hidden; }
  body { background: var(--backdrop); position: relative; font-family: "Open Sans", Arial, sans-serif; }

  .flyer { position: absolute; width: 524px; height: 694px; overflow: hidden; background: var(--panel); box-shadow: 0 2px 8px rgba(0,0,0,.35); }
  .flyer--teal { left: 56px; top: 108px; --photo-a: var(--teal-photo-a); --photo-b: var(--teal-photo-b); --panel: var(--teal-panel); --sweep: var(--teal-sweep); }
  .flyer--olive { left: 628px; top: 203px; --photo-a: var(--olive-photo-a); --photo-b: var(--olive-photo-b); --panel: var(--olive-panel); --sweep: var(--olive-sweep); }

  .hero-photo { position: absolute; left: 0; top: 0; width: 524px; height: 450px; background: linear-gradient(110deg, var(--photo-a) 0%, var(--photo-b) 60%, var(--photo-a) 100%); }
  .hero-curve { position: absolute; left: 0; top: 380px; width: 524px; height: 80px; }

  .headline { position: absolute; font-family: "Bebas Neue", Impact, sans-serif; color: var(--white); font-size: 52px; line-height: 50px; letter-spacing: 1px; }
  .headline--patients { left: 285px; top: 30px; }
  .headline--practice { left: 324px; top: 206px; }

  .section-title { position: absolute; font-family: "Bebas Neue", Impact, sans-serif; color: var(--white); font-size: 30px; letter-spacing: 2.5px; line-height: 30px; }
  .section-title--what { left: 30px; top: 455px; }
  .section-title--who { left: 314px; top: 453px; }
  .col { position: absolute; color: var(--white); }
  .col--what { left: 17px; top: 487px; width: 258px; }
  .col--who { left: 292px; top: 487px; width: 204px; }
  .lead { font-size: 8px; font-weight: 700; line-height: 10.5px; margin-bottom: 6px; }
  .lead--narrow { max-width: 158px; }
  .body-copy { font-size: 7px; line-height: 9px; }

  .contact-bar { position: absolute; left: 0; top: 632px; width: 524px; height: 62px; background: var(--white); color: var(--ink); }
  .brand { position: absolute; left: 24px; top: 14px; display: flex; align-items: center; gap: 6px; }
  .brand-mark { width: 18px; height: 18px; background: var(--teal-photo-a); }
  .brand-name { font-family: "Open Sans", Arial, sans-serif; font-weight: 700; font-size: 12px; color: var(--ink); }
  .office { position: absolute; top: 12px; font-size: 8.8px; font-weight: 700; font-style: italic; line-height: 11px; text-align: center; }
  .office--west { left: 146px; }
  .office--mid { left: 244px; }
  .office--east { left: 386px; }
  .cta { position: absolute; left: 0; width: 524px; top: 41px; text-align: center; font-size: 8.8px; font-weight: 700; font-style: italic; }
</style>
</head>
<body>

<article class="flyer flyer--teal">
  <div class="hero-photo" role="img" aria-label="Photo of a smiling billing specialist wearing a headset at her desk"></div>
  <svg class="hero-curve" viewBox="0 0 524 80" preserveAspectRatio="none" aria-hidden="true">
    <path d="M0 40 Q260 -10 524 18 L524 80 L0 80 Z" fill="var(--sweep)"/>
    <path d="M0 52 Q260 5 524 34 L524 80 L0 80 Z" fill="var(--panel)"/>
  </svg>
  <h1 class="headline headline--patients">You care<br>for your<br>patients</h1>
  <p class="headline headline--practice">We care<br>for your<br>practice</p>

  <h2 class="section-title section-title--what">What we do</h2>
  <h2 class="section-title section-title--who">We are</h2>
  <div class="col col--what">
    <p class="lead">We employ state-of-the-art practice management software to get our clients paid correctly and on time. Through the use of electronic billing (in most cases), we are able to reduce or eliminate denied, rejected, or partially paid insurance claims. We follow up, follow up, and follow up until you get paid.</p>
    <p class="body-copy">Our clients include General Practice as well as several specialists in Colorado, Arizona, Nevada and North Carolina. We provide direct, hands-on management for our doctors and their staff, relieving their need to deal with many of the problems that can crop up with Commercial Carriers, Medicare, Medicaid, and the Blues. Because of our experience in the field, we eliminate most of the problems that occur before they become a problem. All patient information is protected, and their personal files never leave your office.</p>
  </div>
  <div class="col col--who">
    <p class="lead lead--narrow">We are a medical billing/consulting firm who specializes in electronic billing solutions for our customers</p>
    <p class="lead">Our goal is to see your practice become more profitable, while allowing you -the provider- more time and flexibility to do what you do best- care for your patients!</p>
    <p class="body-copy">Our support staff has over 25 years in the medical billing field and tech support for software since 1983. We are also a part of a nationwide network of billing centers with a proven track record of making our clients more profitable. Certified coders and billing specialists insure your claims are transmitted properly and complete- fast.</p>
  </div>

  <footer class="contact-bar">
    <div class="brand"><span class="brand-mark"></span><span class="brand-name">Harbor Claims</span></div>
    <p class="office office--west">Maple Ridge<br>(555) 014-2290</p>
    <p class="office office--mid">Pine Hollow<br>info@harborclaims.net</p>
    <p class="office office--east">Stonebrook<br>fax (555) 014-7731</p>
    <p class="cta">Call us today to arrange a free consultation and evaluation.</p>
  </footer>
</article>

<article class="flyer flyer--olive">
  <div class="hero-photo" role="img" aria-label="Photo of a smiling billing specialist wearing a headset at her desk"></div>
  <svg class="hero-curve" viewBox="0 0 524 80" preserveAspectRatio="none" aria-hidden="true">
    <path d="M0 40 Q260 -10 524 8 L524 80 L0 80 Z" fill="var(--sweep)"/>
    <path d="M0 52 Q260 5 524 40 L524 80 L0 80 Z" fill="var(--panel)"/>
  </svg>
  <h1 class="headline headline--patients">You care<br>for your<br>patients</h1>
  <p class="headline headline--practice">We care<br>for your<br>practice</p>

  <h2 class="section-title section-title--what">What we do</h2>
  <h2 class="section-title section-title--who">We are</h2>
  <div class="col col--what">
    <p class="lead">We employ state-of-the-art practice management software to get our clients paid correctly and on time. Through the use of electronic billing (in most cases), we are able to reduce or eliminate denied, rejected, or partially paid insurance claims. We follow up, follow up, and follow up until you get paid.</p>
    <p class="body-copy">Our clients include General Practice as well as several specialists in Colorado, Arizona, Nevada and North Carolina. We provide direct, hands-on management for our doctors and their staff, relieving their need to deal with many of the problems that can crop up with Commercial Carriers, Medicare, Medicaid, and the Blues. Because of our experience in the field, we eliminate most of the problems that occur before they become a problem. All patient information is protected, and their personal files never leave your office.</p>
  </div>
  <div class="col col--who">
    <p class="lead lead--narrow">We are a medical billing/consulting firm who specializes in electronic billing solutions for our customers</p>
    <p class="lead">Our goal is to see your practice become more profitable, while allowing you -the provider- more time and flexibility to do what you do best- care for your patients!</p>
    <p class="body-copy">Our support staff has over 25 years in the medical billing field and tech support for software since 1983. We are also a part of a nationwide network of billing centers with a proven track record of making our clients more profitable. Certified coders and billing specialists insure your claims are transmitted properly and complete- fast.</p>
  </div>

  <footer class="contact-bar">
    <div class="brand"><span class="brand-mark"></span><span class="brand-name">Harbor Claims</span></div>
    <p class="office office--west">Maple Ridge<br>(555) 014-2290</p>
    <p class="office office--mid">Pine Hollow<br>info@harborclaims.net</p>
    <p class="office office--east">Stonebrook<br>fax (555) 014-7731</p>
    <p class="cta">Call us today to arrange a free consultation and evaluation.</p>
  </footer>
</article>

</body>
</html>
```